Letterhead for Law Firm - Logo already prepared

I previously used to prepare a logo which I was quite pleased with, a copy is attached for your reference. I would like the font of the logo to be all the same size, rather than the 'S' and 'L' being larger than the other letters.
I have copies of the attached in other formats if necessary.
I need a letterhead prepared which is virtually identical to the draft attached, however I will be adding an address, phone number, fax number, mobile number and email. I will provide these details with whoever can assist me.
I will also be providing insurance details to be listed at the foot of the page.
Finally, I need the file to be supplied as a high resolution pdf with 2mm bleed.
If you require any further information, please do not hesitate to contact me.

```html
<!DOCTYPE html>
<html lang="en">
<head>
<meta charset="utf-8">
<title>Marwood Legal – Letterhead</title>
<link rel="stylesheet" href="https://fonts.googleapis.com/css2?family=Marcellus&family=Tinos&display=swap">
<style>
  :root {
    --paper: #ffffff;
    --ink: #1e1e1e;
    --orange-deep: #ee5a24;
    --orange-mid: #f37021;
    --orange-light: #f7941d;
    --orange-line: #f9a51a;
    --footer-text: #ffffff;
  }
  * { margin: 0; padding: 0; box-sizing: border-box; }
  html, body {
    width: 995px;
    height: 1200px;
    overflow: hidden;
    background: var(--paper);
  }
  .letterhead {
    position: relative;
    width: 995px;
    height: 1200px;
    background: var(--paper);
  }
  .brand {
    position: absolute;
    left: 52px;
    top: 37px;
    display: flex;
    align-items: center;
    gap: 20px;
  }
  .brand-mark {
    width: 100px;
    height: 100px;
    border-radius: 50%;
    background: var(--orange-mid);
  }
  .brand-name {
    font-family: "Marcellus", serif;
    font-size: 42px;
    letter-spacing: 1px;
    color: var(--ink);
    text-transform: uppercase;
  }
  .footer-wave {
    position: absolute;
    left: 0;
    top: 0;
    width: 995px;
    height: 1200px;
  }
  .contact {
    position: absolute;
    right: 19px;
    top: 1078px;
    text-align: right;
    font-family: "Tinos", serif;
    color: var(--footer-text);
  }
  .contact-line {
    font-size: 16px;
    line-height: 20px;
    display: flex;
    justify-content: flex-end;
    align-items: center;
    gap: 5px;
  }
  .contact-line svg { width: 11px; height: 11px; fill: var(--footer-text); }
  .address { font-size: 16px; margin-top: 9px; }
  .legal-entity {
    font-size: 13.5px;
    line-height: 16px;
    margin-top: 11px;
  }
</style>
</head>
<body>
  <main class="letterhead">
    <header class="brand">
      <div class="brand-mark"></div>
      <div class="brand-name">Marwood Legal</div>
    </header>

    <svg class="footer-wave" viewBox="0 0 995 1200" preserveAspectRatio="none" aria-hidden="true">
      <defs>
        <linearGradient id="band-fill" x1="0" y1="0" x2="1" y2="0">
          <stop offset="0" stop-color="var(--orange-deep)"/>
          <stop offset="0.5" stop-color="var(--orange-light)"/>
          <stop offset="1" stop-color="var(--orange-deep)"/>
        </linearGradient>
      </defs>
      <path d="M0 1135 C 260 1188, 600 1175, 995 965 L995 1200 L0 1200 Z" fill="url(#band-fill)"/>
      <path d="M0 1160 C 300 1200, 660 1182, 995 1003" fill="none" stroke="var(--orange-line)" stroke-width="3"/>
    </svg>

    <footer class="contact">
      <div class="contact-line">
        <svg viewBox="0 0 24 24"><path d="M6.6 10.8a15.1 15.1 0 0 0 6.6 6.6l2.2-2.2a1 1 0 0 1 1-.25 11.4 11.4 0 0 0 3.6.57 1 1 0 0 1 1 1V20a1 1 0 0 1-1 1A17 17 0 0 1 3 4a1 1 0 0 1 1-1h3.5a1 1 0 0 1 1 1c0 1.25.2 2.45.57 3.57a1 1 0 0 1-.25 1z"/></svg>
        <span>0400 318 572</span>
      </div>
      <div class="contact-line">
        <svg viewBox="0 0 24 24"><path d="M2 6h20v12H2z M2 6l10 7 10-7" stroke="#f37021" stroke-width="1.5"/></svg>
        <span>marwoodlegal@mailbox.com</span>
      </div>
      <div class="address">4/128 Harbour Street, Kingsford 3021</div>
      <div class="legal-entity">
        Marwood Holdings Pty Ltd (ACN 402 118 736) as Trustee for<br>
        the Marwood Family Trust (ABN 51 624 307 982) trading as Marwood Legal
      </div>
    </footer>
  </main>
</body>
</html>
```